Real Estate Newsletter

I would like a template created for a monthly newsletter; ideally, two pages long, including my photo, logo and contact info. I need it to look professional and be very easy for me to drop text into.

Target Market(s)

Past/current clients

Industry/Entity Type

Real Estate Agent

Font styles to use
Serif

Requirements
Must have
• My contact info/photo and logo
• (206) 555-0187
• mkettridge@lunvoro.com
• www.MarlaKettridge.com
Nice to have
• I need a template where I can easily drop contact. I need the template to look professional so I can print it and mail it to current and past clients.

```html
<!DOCTYPE html>
<html lang="en">
<head>
<meta charset="utf-8">
<title>Marla Kettridge Newsletter Letterhead</title>
<link rel="stylesheet" href="https://fonts.googleapis.com/css2?family=Libre+Baskerville:wght@700&family=Arimo:wght@400;700&display=swap">
<style>
  :root {
    --backdrop: #dfe6e6;
    --paper: #ffffff;
    --brand-blue: #283593;
    --ink-grey: #555a60;
    --photo-light: #efe9e2;
    --photo-mid: #a98466;
    --photo-dark: #5b4131;
  }
  * { margin: 0; padding: 0; box-sizing: border-box; }
  html, body {
    width: 1200px; height: 891px; overflow: hidden;
    background: var(--backdrop);
  }
  .letterhead {
    position: absolute;
    left: 280px; top: 28px;
    width: 640px; height: 835px;
    background: var(--paper);
    box-shadow: 0 6px 24px rgba(0,0,0,0.12);
    overflow: hidden;
  }
  .brand-name {
    position: absolute;
    left: 46px; top: 44px;
    font-family: "Libre Baskerville", serif;
    font-weight: 700;
    font-size: 24px;
    color: var(--brand-blue);
    letter-spacing: 0.2px;
  }
  .contact-block {
    position: absolute;
    right: 40px; top: 46px;
    text-align: right;
    font-family: "Arimo", sans-serif;
    font-size: 12px;
    line-height: 16px;
    color: var(--ink-grey);
  }
  .edge-tab {
    position: absolute;
    right: 0; top: 44px;
    width: 8px; height: 34px;
    background: var(--brand-blue);
  }
  .agent-photo {
    position: absolute;
    left: 330px; bottom: 0;
    width: 240px; height: 230px;
    background: radial-gradient(ellipse at 50% 40%, var(--photo-light) 0%, var(--photo-mid) 55%, var(--photo-dark) 100%);
    border-radius: 120px 120px 0 0;
  }
  .footer-band {
    position: absolute;
    left: 0; bottom: 0;
    width: 360px; height: 96px;
  }
  .website {
    position: absolute;
    left: 0; bottom: 24px;
    width: 300px;
    text-align: right;
    font-family: "Arimo", sans-serif;
    font-size: 15px;
    color: #ffffff;
  }
  .website strong { font-weight: 700; }
</style>
</head>
<body>
  <main class="letterhead">
    <div class="brand-name">Marla Kettridge</div>

    <div class="contact-block">
      <div class="contact-phone">(206) 555-0187</div>
      <div class="contact-email">mkettridge@lunvoro.com</div>
    </div>
    <div class="edge-tab"></div>

    <div class="agent-photo" role="img" aria-label="Portrait photo of the agent, smiling, in a light patterned blouse"></div>

    <svg class="footer-band" viewBox="0 0 360 96" aria-hidden="true">
      <polygon points="0,0 300,34 360,96 0,96" fill="var(--brand-blue)"/>
    </svg>
    <div class="website">www.<strong>MarlaKettridge</strong>.com</div>
  </main>
</body>
</html>
```